Want to incorporate elements of all these items to make an amazing sign to welcome people to the community. The sign is 6x4 and needs to incorporate the following items:

Welcome to Corwick Meadows

Come visit the PRD sales center at 745 thistledown road
High Speed Fiber Internet
Land financing starting at $299 (No credit checks)
Let us build your dream home!
555-284-7390
We like the gold and black design no teal or blue that was another agents design. Some combination of the current sign all the stuff listed above and then design elements that tie into the truck wrap.

Target Market(s)

People visiting the neighborhood

Industry/Entity Type

real estate and construction

Font styles to use
Serif

Colors

Designer to choose colors to be used in the design.

Requirements
Must have
• PRD Home Builders Welcomes you to Corwick Meadows, Let us build your dream home, Phone number, Land financing starting at $299 NO credit checks

```html
<!DOCTYPE html>
<html lang="en">
<head>
<meta charset="utf-8">
<title>Corwick Meadows Welcome Sign</title>
<link href="https://fonts.googleapis.com/css2?family=Great+Vibes&family=Montserrat:wght@800&family=Source+Sans+3:wght@500;600&display=swap" rel="stylesheet">
<style>
  :root {
    --page: #ffffff;
    --ink: #000000;
    --paper: #ffffff;
    --sign-edge: #9a9a9a;
    --plan-light: #d9d9dc;
    --plan-mid: #a9a9ad;
    --print-light: #dedede;
    --print-mid: #9c9c9c;
    --gold-light: #f6dc86;
    --gold: #d7a93c;
    --gold-deep: #9b6a14;
  }
  * { margin: 0; padding: 0; box-sizing: border-box; }
  html, body {
    width: 1200px; height: 1000px; overflow: hidden;
    background: var(--page);
  }
  .sign {
    position: absolute; left: 128px; top: 185px;
    width: 945px; height: 630px;
    background: var(--ink);
    border: 1px solid var(--sign-edge);
    overflow: hidden;
  }
  .photo { position: absolute; top: 0; height: 100%; }
  .photo--plan {
    left: 0; width: 420px;
    background: linear-gradient(to right, var(--plan-light) 0%, var(--plan-mid) 45%, rgba(0,0,0,0) 100%);
  }
  .photo--prints {
    right: 0; width: 400px;
    background: linear-gradient(to left, var(--print-light) 0%, var(--print-mid) 45%, rgba(0,0,0,0) 100%);
  }
  .outlined {
    color: var(--paper);
    text-shadow:
      -2px -2px 0 var(--ink), 2px -2px 0 var(--ink), -2px 2px 0 var(--ink), 2px 2px 0 var(--ink),
      0 -2px 0 var(--ink), 0 2px 0 var(--ink), -2px 0 0 var(--ink), 2px 0 0 var(--ink),
      3px 3px 2px rgba(0,0,0,.6);
  }
  .line { position: absolute; white-space: nowrap; text-align: center; }
  .welcome {
    left: 0; width: 100%; top: 68px;
    font-family: "Great Vibes", cursive; font-weight: 400;
    font-size: 78px; line-height: 1.1;
  }
  .visit {
    left: 0; width: 100%; top: 192px; line-height: 1;
    display: flex; justify-content: center; align-items: center; gap: 22px;
    font-family: "Source Sans 3", sans-serif; font-weight: 600;
    font-size: 38px; letter-spacing: -1px;
  }
  .gold {
    background: linear-gradient(to bottom, var(--gold-light) 0%, var(--gold) 50%, var(--gold-deep) 100%);
    -webkit-background-clip: text; background-clip: text;
    color: transparent;
    filter: drop-shadow(3px 3px 0 var(--ink));
    font-family: "Montserrat", sans-serif; font-weight: 800;
  }
  .builder-name { font-size: 108px; line-height: 1; letter-spacing: -2px; }
  .feature {
    font-family: "Source Sans 3", sans-serif; font-weight: 500;
    line-height: 1.2;
  }
  .feature--internet { left: 50px; width: 196px; top: 314px; font-size: 25px; }
  .feature--address  { left: 290px; width: 365px; top: 314px; font-size: 24px; color: var(--paper); }
  .feature--finance  { left: 680px; width: 220px; top: 307px; font-size: 20px; line-height: 1.3; }
  .tagline {
    left: 0; width: 100%; top: 402px;
    font-family: "Source Sans 3", sans-serif; font-weight: 600;
    font-size: 49px; letter-spacing: -0.5px; line-height: 1.2;
  }
  .phone {
    left: 0; width: 100%; top: 474px;
    font-size: 108px; line-height: 1.1;
  }
</style>
</head>
<body>
  <main class="sign">
    <div class="photo photo--plan" role="img" aria-label="Hand sketching with a pencil on a subdivision lot plan"></div>
    <div class="photo photo--prints" role="img" aria-label="Rolled architectural blueprints over a floor plan"></div>

    <h1 class="line welcome outlined">Welcome to Corwick Meadows</h1>

    <p class="line visit">
      <span class="outlined">COME VISIT THE</span>
      <span class="gold builder-name">PRD</span>
      <span class="outlined">SALES CENTER</span>
    </p>

    <p class="line feature feature--internet outlined">High Speed<br>Fiber Internet</p>
    <p class="line feature feature--address">AT 745 THISTLEDOWN ROAD</p>
    <p class="line feature feature--finance outlined">LAND FINANCING<br>STARTING AT $299<br>(NO CREDIT CHECKS)</p>

    <p class="line tagline outlined">Let us build your dream home!</p>
    <p class="line phone gold">555-284-7390</p>
  </main>
</body>
</html>
```